Dr. Pell Works
Business card, stationary, fax page, envelope
Dr. Pell Works - Corporate Services
Creative Brief
Bright & Fun-filled
Grant Bevis Hallworth
Senior Account Executive
417 S. Tavish Ave Los Angeles CA 90012
grant@drpellworks.example
drpellworks.example
I also have 4 other people that need their won business cards but with their cell phone and title info.

```html
<!DOCTYPE html>
<html lang="en">
<head>
<meta charset="utf-8">
<title>Dr. Pell Works – Business Card</title>
<link rel="stylesheet" href="https://fonts.googleapis.com/css2?family=PT+Sans:wght@400;700&display=swap">
<style>
  :root {
    --page-bg: #ecebe8;
    --card-white: #ffffff;
    --copper-dark: #b8643c;
    --copper-light: #eeb08a;
    --rule: #1c1c1c;
    --accent: #e0701e;
    --ink: #2b2b2b;
    --ink-soft: #3c3c3c;
    --brand-grey: #4b4b4b;
    --mark-fill: #f2c9a8;
  }
  * { box-sizing: border-box; margin: 0; padding: 0; }
  html, body {
    width: 1200px; height: 965px; overflow: hidden;
    background: var(--page-bg);
    font-family: "PT Sans", Arial, sans-serif;
  }
  .card {
    position: absolute; left: 215px; top: 248px;
    width: 770px; height: 468px;
    background: var(--card-white);
    border-radius: 22px;
    overflow: hidden;
    box-shadow: 0 6px 18px rgba(0,0,0,0.18);
  }
  .band {
    position: absolute; left: 0; right: 0; height: 26px;
    background: linear-gradient(90deg, var(--copper-dark), var(--copper-light) 50%, var(--copper-dark));
  }
  .band--top { top: 0; }
  .band--bottom { bottom: 0; }
  .rule {
    position: absolute; left: 0; right: 0; height: 3px; background: var(--rule);
  }
  .rule--top { top: 31px; }
  .rule--bottom { bottom: 31px; }

  .brand { position: absolute; left: 90px; top: 52px; display: flex; align-items: center; gap: 24px; }
  .brand__mark {
    width: 112px; height: 112px; border-radius: 50%;
    background: var(--mark-fill);
  }
  .brand__name {
    font-weight: 700; font-size: 66px; line-height: 1;
    color: var(--brand-grey); letter-spacing: 0.5px;
  }

  .person {
    position: absolute; right: 398px; top: 282px; text-align: right;
  }
  .person__name { font-size: 28px; font-weight: 700; color: var(--accent); line-height: 1.1; }
  .person__title { font-size: 18px; font-weight: 700; color: var(--ink); margin-top: 6px; }
  .person__address { font-size: 18px; color: var(--ink-soft); margin-top: 22px; line-height: 1.55; }

  .divider {
    position: absolute; left: 398px; top: 212px; width: 2px; height: 180px;
    background: #9a9a9a;
  }

  .contacts { position: absolute; left: 414px; top: 214px; list-style: none; }
  .contacts li {
    display: flex; align-items: center; gap: 14px;
    height: 31px; font-size: 18px; color: var(--ink-soft);
  }
  .contacts svg { width: 18px; height: 18px; fill: var(--accent); flex: none; }
</style>
</head>
<body>
  <div class="card">
    <div class="band band--top"></div>
    <div class="rule rule--top"></div>

    <div class="brand">
      <div class="brand__mark" role="img" aria-label="Brand mascot area"></div>
      <div class="brand__name">Dr. Pell Works</div>
    </div>

    <div class="person">
      <div class="person__name">Grant Bevis Hallworth</div>
      <div class="person__title">Senior Account Executive</div>
      <div class="person__address">417 S. Tavish Ave<br>Los Angeles CA 90012</div>
    </div>

    <div class="divider"></div>

    <ul class="contacts">
      <li>
        <svg viewBox="0 0 24 24" aria-hidden="true"><path d="M6.6 10.8a15.1 15.1 0 0 0 6.6 6.6l2.2-2.2c.3-.3.7-.4 1-.2 1.1.4 2.3.6 3.6.6.6 0 1 .4 1 1V20c0 .6-.4 1-1 1A17 17 0 0 1 3 4c0-.6.4-1 1-1h3.5c.6 0 1 .4 1 1 0 1.3.2 2.5.6 3.6.1.3 0 .7-.2 1z"/></svg>
        323-555-0142
      </li>
      <li>
        <svg viewBox="0 0 24 24" aria-hidden="true"><path d="M8 1h8a2 2 0 0 1 2 2v18a2 2 0 0 1-2 2H8a2 2 0 0 1-2-2V3a2 2 0 0 1 2-2zm0 3v13h8V4zm4 15a1.2 1.2 0 1 0 0 2.4 1.2 1.2 0 0 0 0-2.4z"/></svg>
        310-555-0187
      </li>
      <li>
        <svg viewBox="0 0 24 24" aria-hidden="true"><path d="M6 2h9l3 3v5H6zm-2 10h16a2 2 0 0 1 2 2v6a2 2 0 0 1-2 2H4a2 2 0 0 1-2-2v-6a2 2 0 0 1 2-2zm3 3v2h4v-2zm9 0v2h2v-2z"/></svg>
        323-555-0163
      </li>
      <li>
        <svg viewBox="0 0 24 24" aria-hidden="true"><path d="M12 2a10 10 0 1 0 5 18.7l-1-1.7A8 8 0 1 1 20 12v1a2 2 0 0 1-4 0V7h-2v1a5 5 0 1 0 .6 7.4A4 4 0 0 0 22 13v-1A10 10 0 0 0 12 2zm0 7a3 3 0 1 1 0 6 3 3 0 0 1 0-6z"/></svg>
        grant@drpellworks.example
      </li>
      <li>
        <svg viewBox="0 0 24 24" aria-hidden="true"><path d="M12 2a10 10 0 1 0 0 20 10 10 0 0 0 0-20zm6.9 9h-3a15 15 0 0 0-1.3-6.3A8 8 0 0 1 18.9 11zM12 4c.9 1.2 1.8 3.7 1.9 7h-3.8c.1-3.3 1-5.8 1.9-7zM9.4 4.7A15 15 0 0 0 8.1 11h-3a8 8 0 0 1 4.3-6.3zM5.1 13h3a15 15 0 0 0 1.3 6.3A8 8 0 0 1 5.1 13zM12 20c-.9-1.2-1.8-3.7-1.9-7h3.8c-.1 3.3-1 5.8-1.9 7zm2.6-.7a15 15 0 0 0 1.3-6.3h3a8 8 0 0 1-4.3 6.3z"/></svg>
        drpellworks.example
      </li>
    </ul>

    <div class="rule rule--bottom"></div>
    <div class="band band--bottom"></div>
  </div>
</body>
</html>
```